We are an integrated facilities management company.

We aggregate everything related to facilities maintenance. Repair-replacement of equipment and facility space materials from:
Asset gathering and tracking.
Vendor screening, contracting and management.
Service requirement development.
Work order processing and management.
Invoice reconciliation.
Vendor payment.
Reporting.
Capital equipment bids and project management.

Target Market(s)

Retail, hospitality, multi-family housing, long term healthcare.

Industry/Entity Type

Maintenance

Contact Information for Business Card

Professional and bold look. (see logo zip file)

Colors
3377b5
85abd2
cedeed

Requirements
Must have
• N/A
Nice to have
• N/A
Should not have
• N/A

```html
<!DOCTYPE html>
<html lang="en">
<head>
<meta charset="utf-8">
<title>Keystone Facility Partners – Business Card</title>
<link rel="stylesheet" href="https://fonts.googleapis.com/css2?family=Roboto:ital,wght@0,400;0,700;0,900;1,400&family=Roboto+Condensed:wght@700&display=swap">
<style>
  :root {
    --blue: #3377b5;
    --blue-mid: #85abd2;
    --blue-pale: #cedeed;
    --ink: #111418;
    --rule: #c9ccd0;
    --white: #ffffff;
    --backdrop: #2b2e33;
  }
  * { box-sizing: border-box; margin: 0; padding: 0; }
  html, body {
    width: 1200px; height: 900px; overflow: hidden;
    background: var(--backdrop);
  }
  .stage {
    position: relative; width: 1200px; height: 900px;
    display: flex; flex-direction: column; align-items: center; justify-content: center; gap: 44px;
  }
  .card {
    position: relative; width: 630px; height: 360px; overflow: hidden;
    border-radius: 3px; box-shadow: 0 14px 30px rgba(0,0,0,.45);
  }

  /* Contact side */
  .card--front { background: var(--white); }
  .card--front .edge-band {
    position: absolute; left: 0; right: 0; bottom: 0; height: 10px; background: var(--blue);
  }
  .card--front .divider {
    position: absolute; inset: 0; width: 100%; height: 100%;
  }
  .brand {
    position: absolute; display: flex; align-items: center; gap: 10px;
  }
  .brand__mark { width: 30px; height: 30px; background: var(--blue); flex: none; }
  .brand__name {
    font-family: "Roboto Condensed", "Roboto", sans-serif; font-weight: 700;
    color: var(--blue); text-transform: uppercase; line-height: 1.05;
  }
  .card--front .brand { left: 36px; top: 78px; }
  .card--front .brand__name { font-size: 19px; }

  .person { position: absolute; left: 370px; top: 62px; }
  .person__name {
    font-family: "Roboto", sans-serif; font-weight: 900; font-size: 25px;
    color: var(--ink); text-transform: uppercase; letter-spacing: .01em;
  }
  .person__title {
    font-family: "Roboto", sans-serif; font-style: italic; font-size: 18px;
    color: var(--blue); margin-top: 2px;
  }
  .contacts { position: absolute; left: 330px; top: 160px; list-style: none; }
  .contacts li {
    display: flex; align-items: center; gap: 12px; height: 34px;
    font-family: "Roboto", sans-serif; font-size: 21px; color: var(--ink);
  }
  .contacts svg { width: 18px; height: 18px; flex: none; fill: var(--blue); }

  /* Brand side */
  .card--back { background: var(--blue-mid); }
  .card--back .center-band {
    position: absolute; left: 0; right: 0; top: 108px; height: 144px;
    background: var(--white); display: flex; align-items: center; justify-content: center;
  }
  .card--back .brand { position: static; gap: 14px; }
  .card--back .brand__mark { width: 44px; height: 44px; }
  .card--back .brand__name { font-size: 30px; }
</style>
</head>
<body>
<main class="stage">

  <section class="card card--front" aria-label="Business card, contact side">
    <svg class="divider" viewBox="0 0 630 360" aria-hidden="true">
      <line x1="322" y1="40" x2="245" y2="300" stroke="var(--rule)" stroke-width="1.5"/>
      <polygon points="0,315 240,315 230,350 0,350" fill="var(--blue-pale)"/>
    </svg>

    <div class="brand">
      <span class="brand__mark"></span>
      <span class="brand__name">Keystone<br>Facility Partners</span>
    </div>

    <div class="person">
      <h1 class="person__name">Dara Olsen</h1>
      <p class="person__title">Your Title Here</p>
    </div>

    <ul class="contacts">
      <li>
        <svg viewBox="0 0 24 24" aria-hidden="true"><path d="M6.6 10.8a15.1 15.1 0 0 0 6.6 6.6l2.2-2.2c.3-.3.7-.4 1-.2 1.1.4 2.3.6 3.6.6.6 0 1 .4 1 1V20c0 .6-.4 1-1 1A17 17 0 0 1 3 4c0-.6.4-1 1-1h3.5c.6 0 1 .4 1 1 0 1.3.2 2.5.6 3.6.1.3 0 .7-.2 1z"/></svg>
        012 555 0147
      </li>
      <li>
        <svg viewBox="0 0 24 24" aria-hidden="true"><path d="M2 5h20v2l-10 6L2 7zM2 9l10 6 10-6v10H2z"/></svg>
        youremail@here.com
      </li>
      <li>
        <svg viewBox="0 0 24 24" aria-hidden="true"><path d="M12 2a10 10 0 1 0 0 20 10 10 0 0 0 0-20zm0 3a7 7 0 0 1 6.9 6h-3.4a11 11 0 0 0-1.6-5.7A7 7 0 0 1 12 5zm-2 .3A11 11 0 0 0 8.5 11H5.1A7 7 0 0 1 10 5.3zM5.1 13h3.4a11 11 0 0 0 1.5 5.7A7 7 0 0 1 5.1 13zm8.8 5.7a11 11 0 0 0 1.6-5.7h3.4a7 7 0 0 1-5 5.7z"/></svg>
        yourwebsitehere.com
      </li>
      <li>
        <svg viewBox="0 0 24 24" aria-hidden="true"><path d="M22 2 2 10.5l7.5 2.5L12 21z"/></svg>
        youraddresshere#123
      </li>
    </ul>

    <div class="edge-band"></div>
  </section>

  <section class="card card--back" aria-label="Business card, brand side">
    <div class="center-band">
      <div class="brand">
        <span class="brand__mark"></span>
        <span class="brand__name">Keystone<br>Facility Partners</span>
      </div>
    </div>
  </section>

</main>
</body>
</html>
```